iOS7 test prep app

I need 3 basic screens and 2 product images for an iOS7 app I am prototyping. I provided lots of detail in the attached brief. This is an education product, so warm colors (especially reds) work best.

If you've done flat design for mobile products, please take a look ... Thanks!

Greetings, all. Thank you for your submissions. I am meeting with my product development team this week to review your submissions, and will select a designer before the end of the week. I appreciate your patience with my process, and thank you again for your interest in my project. I'll be back to you soon ... -Dorian

```html
<!DOCTYPE html>
<html lang="en">
<head>
<meta charset="utf-8">
<title>MindPrep Mobile Exam Prep – Dashboard</title>
<link href="https://fonts.googleapis.com/css2?family=Roboto:wght@300;400;500&family=Roboto+Condensed:wght@400;700&display=swap" rel="stylesheet">
<style>
  :root{
    --stage:#ece5f7;
    --screen:#e6e6e6;
    --card:#ffffff;
    --orange:#ef900d;
    --orange-light:#f6a82a;
    --ink:#1d1d1d;
    --muted:#7a7a7a;
    --score-orange:#f39a12;
    --score-red:#e0262e;
    --up-green:#38b82c;
    --down-red:#e0262e;
    --gauge:#353535;
    --gauge-blue:#3b9ae6;
  }
  *{box-sizing:border-box;margin:0;padding:0}
  html,body{width:1200px;height:1000px;overflow:hidden;background:var(--stage)}
  body{font-family:"Roboto",sans-serif;color:var(--ink)}
  .screen{
    position:absolute;left:330px;top:21px;width:540px;height:958px;
    background:var(--screen);overflow:hidden;
    box-shadow:0 20px 50px rgba(60,40,100,.18);
  }
  .app-header{
    height:110px;color:#fff;
    background:linear-gradient(90deg,var(--orange),var(--orange-light));
  }
  .status-bar{
    display:flex;justify-content:space-between;align-items:center;
    height:36px;padding:0 14px;font-size:16px;font-weight:400;
  }
  .status-left,.status-right{display:flex;align-items:center;gap:6px;width:160px}
  .status-right{justify-content:flex-end}
  .signal{letter-spacing:1px;font-size:11px}
  .app-title{
    text-align:center;font-family:"Roboto Condensed",sans-serif;
    font-weight:700;font-size:27px;line-height:62px;
  }
  .dashboard{
    display:grid;grid-template-columns:1fr 1fr;
    grid-template-rows:210px 215px 235px;gap:12px;padding:12px;
  }
  .card{background:var(--card);padding:14px 16px;position:relative}
  .card-title{
    font-family:"Roboto Condensed",sans-serif;font-weight:700;
    font-size:19px;text-transform:uppercase;text-align:center;margin-bottom:12px;
  }
  .card.wide{grid-column:1 / 3}
  .stat-row{
    display:flex;justify-content:space-between;align-items:center;
    font-size:17px;color:var(--muted);font-family:"Roboto Condensed",sans-serif;
    line-height:30px;
  }
  .stat-row b{font-family:"Roboto",sans-serif;font-weight:500}
  .val-orange{color:var(--score-orange)}
  .val-red{color:var(--score-red)}
  .val-green{color:var(--up-green)}
  .val-ink{color:var(--ink)}
  .up{color:var(--up-green)}
  .down{color:var(--down-red)}
  .up-red{color:var(--down-red)}
  .down-green{color:var(--up-green)}
  .arrow{font-size:22px;font-weight:300;width:24px;text-align:center}
  .booster-row{
    display:grid;grid-template-columns:1fr 1fr 30px;align-items:center;
    font-family:"Roboto Condensed",sans-serif;font-size:18px;color:var(--muted);line-height:34px;
  }
  .readiness{text-align:center}
  .readiness-value{font-weight:300;font-size:44px;color:var(--gauge-blue);line-height:44px}
  .gauge{display:block;margin:0 auto}
  .trend-grid{display:grid;grid-template-columns:1fr 1fr;column-gap:34px;padding:0 6px}
  .trend-row{
    display:grid;grid-template-columns:1fr 56px 26px;align-items:center;
    font-family:"Roboto Condensed",sans-serif;font-size:18px;color:var(--muted);line-height:40px;
  }
  .trend-row b{font-family:"Roboto",sans-serif;font-weight:500;font-size:20px;text-align:right;padding-right:8px}
  .distribution{position:relative}
  .pie-label{
    position:absolute;font-family:"Roboto Condensed",sans-serif;font-weight:700;font-size:13px;
  }
  .begin-test{
    position:absolute;left:40px;right:40px;top:830px;height:110px;
    background:var(--orange);color:#fff;border:0;
    font-family:"Roboto Condensed",sans-serif;font-size:30px;text-transform:uppercase;
    display:flex;align-items:center;justify-content:center;
  }
</style>
</head>
<body>
<main class="screen">
  <header class="app-header">
    <div class="status-bar">
      <div class="status-left">
        <span class="signal">●●●●○</span><span>Carrier</span>
        <svg width="16" height="12" viewBox="0 0 16 12" aria-hidden="true"><path d="M1 4a10 10 0 0 1 14 0M3.5 6.5a6.5 6.5 0 0 1 9 0M6 9a3 3 0 0 1 4 0" fill="none" stroke="#fff" stroke-width="1.6" stroke-linecap="round"/></svg>
      </div>
      <span class="status-time">7:28 PM</span>
      <div class="status-right">
        <span>100%</span>
        <svg width="28" height="12" viewBox="0 0 28 12" aria-hidden="true"><rect x="0.5" y="0.5" width="24" height="11" rx="2" fill="#fff" stroke="#fff"/><rect x="25" y="4" width="2" height="4" fill="#fff"/></svg>
      </div>
    </div>
    <h1 class="app-title">MindPrep Mobile Exam Prep</h1>
  </header>

  <section class="dashboard">
    <article class="card key-stats">
      <h2 class="card-title">Key Stats</h2>
      <div class="stat-row"><span>Total Tests:</span><b class="val-ink">6</b></div>
      <div class="stat-row"><span>Last Score:</span><b class="val-orange">68%</b></div>
      <div class="stat-row"><span>Cum. Score:</span><b class="val-red">59%</b></div>
      <div class="stat-row"><span>Trend:</span><span class="arrow up">↑</span></div>
    </article>

    <article class="card readiness">
      <h2 class="card-title">Readiness Meter</h2>
      <div class="readiness-value">65%</div>
      <svg class="gauge" width="220" height="118" viewBox="0 0 220 118" aria-label="Readiness gauge at 65%">
        <path d="M40 100 A70 70 0 0 1 180 100" fill="none" stroke="var(--gauge)" stroke-width="46"/>
        <line x1="110" y1="100" x2="139" y2="44" stroke="#cfcfcf" stroke-width="6" stroke-linecap="round"/>
        <circle cx="110" cy="100" r="11" fill="#fff" stroke="var(--gauge-blue)" stroke-width="5"/>
        <text x="4" y="114" font-family="Roboto Condensed, sans-serif" font-size="11" fill="#8a8a8a">NOT READY</text>
        <text x="176" y="114" font-family="Roboto Condensed, sans-serif" font-size="11" fill="#8a8a8a">READY</text>
      </svg>
    </article>

    <article class="card boosters">
      <h2 class="card-title">Booster Levels</h2>
      <div class="booster-row"><span>HP</span><span>5x</span><span class="arrow up-red">↑</span></div>
      <div class="booster-row"><span>PI</span><span>5x</span><span class="arrow up-red">↑</span></div>
      <div class="booster-row"><span>PA</span><span>4x</span><span class="arrow down-green">↓</span></div>
      <div class="booster-row"><span>CM</span><span>3x</span><span class="arrow down-green">↓</span></div>
    </article>

    <article class="card distribution">
      <h2 class="card-title">Test Plan Distribution</h2>
      <svg class="pie" width="150" height="150" viewBox="-75 -75 150 150" style="position:absolute;left:51px;top:50px" aria-label="Test plan distribution pie chart">
        <g transform="rotate(-90)" fill="none" stroke-width="72">
          <circle r="36" pathLength="100" stroke="#7b2fc4" stroke-dasharray="12 100" stroke-dashoffset="0"/>
          <circle r="36" pathLength="100" stroke="#2a8fe8" stroke-dasharray="14 100" stroke-dashoffset="-12"/>
          <circle r="36" pathLength="100" stroke="#2fae2a" stroke-dasharray="20 100" stroke-dashoffset="-26"/>
          <circle r="36" pathLength="100" stroke="#f3c514" stroke-dasharray="12 100" stroke-dashoffset="-46"/>
          <circle r="36" pathLength="100" stroke="#ef8d16" stroke-dasharray="15 100" stroke-dashoffset="-58"/>
          <circle r="36" pathLength="100" stroke="#e2302a" stroke-dasharray="9 100" stroke-dashoffset="-73"/>
          <circle r="36" pathLength="100" stroke="#b3142a" stroke-dasharray="9 100" stroke-dashoffset="-82"/>
          <circle r="36" pathLength="100" stroke="#d11f4a" stroke-dasharray="9 100" stroke-dashoffset="-91"/>
        </g>
        <g font-family="Roboto, sans-serif" font-size="10" fill="#fff" text-anchor="middle" dominant-baseline="middle">
          <text x="17" y="-42">12%</text><text x="42" y="-17">14%</text><text x="35" y="29">20%</text>
          <text x="-6" y="45">12%</text><text x="-37" y="25">15%</text><text x="-44" y="-7">9%</text>
          <text x="-34" y="-30">9%</text><text x="-13" y="-43">9%</text>
        </g>
      </svg>
      <span class="pie-label" style="left:40px;top:48px;color:#7b2fc4">S&amp;MC</span>
      <span class="pie-label" style="left:14px;top:76px;color:#b3142a">HP&amp;M</span>
      <span class="pie-label" style="left:14px;top:110px;color:#e2302a">PI</span>
      <span class="pie-label" style="left:14px;top:142px;color:#e2302a">BC&amp;C</span>
      <span class="pie-label" style="left:110px;top:192px;color:#ef8d16">P&amp;PT</span>
      <span class="pie-label" style="left:200px;top:172px;color:#e0b000">RRP</span>
      <span class="pie-label" style="left:212px;top:140px;color:#2fae2a">MC</span>
      <span class="pie-label" style="left:212px;top:100px;color:#2a8fe8">PA</span>
    </article>

    <article class="card wide trending">
      <h2 class="card-title">Trending Performance by Category</h2>
      <div class="trend-grid">
        <div class="trend-col">
          <div class="trend-row"><span>Care Mgt</span><b class="val-orange">68%</b><span class="arrow down">↓</span></div>
          <div class="trend-row"><span>Safety IC</span><b class="val-orange">68%</b><span class="arrow up">↑</span></div>
          <div class="trend-row"><span>HP &amp; M</span><b class="val-red">59%</b><span class="arrow up">↑</span></div>
          <div class="trend-row"><span>PI</span><b class="val-red">44%</b><span class="arrow down">↓</span></div>
        </div>
        <div class="trend-col">
          <div class="trend-row"><span>Basic C &amp; C</span><b class="val-green">77%</b><span class="arrow down">↓</span></div>
          <div class="trend-row"><span>Pharma PT</span><b class="val-orange">67%</b><span class="arrow up">↑</span></div>
          <div class="trend-row"><span>Risk</span><b class="val-orange">58%</b><span class="arrow up">↑</span></div>
          <div class="trend-row"><span>PA</span><b class="val-red">43%</b><span class="arrow down">↓</span></div>
        </div>
      </div>
    </article>
  </section>

  <button class="begin-test" type="button">Begin Test</button>
</main>
</body>
</html>
```